Home Health Care Agency Needs a Website (Seeking a PSD)

We need a user friendly website for a Home Health Care Agency. Our service is for the elderly and disabled. Frequently the busy professional middle-aged married daughter will use the website to arrange in-home care for an aging parent. Therefore, our website is primarily geared towards middle-aged women. In-home care is typically 24 hours a day so, a feeling of trustworthiness and security should be effectively conveyed. (Seeking a PSD- however, if you also offer coding, please let us know the cost.)

Target Market(s)

Frequently the busy professional middle-aged married daughter (possibly out of state) will use the website to arrange in-home care for an aging parent.

Industry/Entity Type

Security

Requirements
Must have
• Website must be clean, uncluttered and professional. The following menu pages are requested: Home, About Us, Services, Resources, FAQ, Employment & Contact.
Should not have
• Must not be too whimsical.

```html
<!DOCTYPE html>
<html lang="en">
<head>
<meta charset="utf-8">
<title>Meadowlight Home Care</title>
<link rel="stylesheet" href="https://fonts.googleapis.com/css2?family=Gelasio:wght@400&family=Tinos:wght@400&family=Signika:wght@400;600&family=Arimo:wght@400&display=swap">
<style>
  :root {
    --page-bg: #f1f1f1;
    --white: #ffffff;
    --sky: #4cc5ec;
    --sky-deep: #2fb0dc;
    --sky-fold: #1f8fb8;
    --ink: #5e5e5e;
    --ink-soft: #7a7a7a;
    --rule: #b9b9b9;
    --band: #d7eef6;
    --band-light: #e6f5fa;
    --footer: #434244;
    --button: #a9a9a9;
  }
  * { margin: 0; padding: 0; box-sizing: border-box; }
  html, body { width: 1091px; height: 1200px; overflow: hidden; }
  body { position: relative; background: var(--page-bg); font-family: "Tinos", serif; color: var(--ink); }
  .page { position: absolute; left: 64px; top: 0; width: 963px; height: 1132px; background: var(--white); }

  .brand { position: absolute; left: 118px; top: 62px; display: flex; align-items: center; gap: 10px; }
  .brand-dot { width: 18px; height: 18px; border-radius: 50%; background: var(--sky); }
  .brand-name { font-family: "Signika", sans-serif; font-weight: 600; font-size: 25px; color: var(--sky-deep); line-height: 1.05; }

  .social { position: absolute; top: 80px; left: 873px; display: flex; gap: 9px; list-style: none; }
  .social li { width: 26px; height: 26px; border-radius: 50%; }
  .social li:nth-child(1) { background: #4a90c9; }
  .social li:nth-child(2) { background: #3b5597; }
  .social li:nth-child(3) { background: #1e7ab6; }

  .ribbon { position: absolute; top: 159px; width: 64px; height: 46px; background: var(--sky-deep); }
  .ribbon.left { left: 0; }
  .ribbon.right { right: 0; width: 64px; }
  .main-nav { position: absolute; left: 41px; top: 138px; width: 1007px; height: 46px; background: var(--sky); }
  .main-nav a { position: absolute; top: 12px; transform: translateX(-50%); font-family: "Gelasio", serif; font-size: 17px; letter-spacing: 1px; color: var(--white); text-decoration: none; white-space: nowrap; }

  .hero { position: absolute; left: 72px; top: 184px; width: 951px; height: 413px;
    background: linear-gradient(100deg, #ece9e3 0%, #d9d3ca 30%, #5a9fc1 48%, #c9a98a 62%, #b07a52 75%, #2aa6c9 100%); }
  .hero-title { position: absolute; left: 76px; top: 36px; font-family: "Signika", sans-serif; font-size: 28px; color: var(--ink); }
  .hero-title em, .hero-sub em { font-style: normal; color: var(--sky-deep); }
  .hero-sub { position: absolute; left: 67px; top: 66px; font-family: "Signika", sans-serif; font-size: 15px; letter-spacing: .5px; color: var(--ink); }
  .hero-button { position: absolute; left: 68px; top: 98px; width: 198px; height: 45px; border: 1px solid #d0d0d0; background: rgba(255,255,255,.55);
    font-family: "Arimo", sans-serif; font-size: 16px; color: #8a8a8a; display: flex; align-items: center; padding-left: 10px; gap: 6px; }
  .hero-arrow { position: absolute; top: 178px; width: 44px; height: 44px; border-radius: 50%; background: rgba(80,80,80,.55); }
  .hero-arrow svg { display: block; }
  .hero-arrow.prev { left: 2px; }
  .hero-arrow.next { right: 9px; }
  .hero-dots { position: absolute; left: 437px; top: 395px; display: flex; gap: 10px; }
  .hero-dots span { width: 11px; height: 11px; border-radius: 50%; background: rgba(70,70,70,.6); }

  .section-title { position: absolute; left: 140px; width: 829px; text-align: center; font-family: "Gelasio", serif; font-size: 21px; letter-spacing: 1px; color: var(--ink-soft); }
  .rule { position: absolute; left: 140px; width: 829px; height: 1px; background: var(--rule); }
  .welcome-text { position: absolute; left: 150px; top: 677px; width: 809px; text-align: center; font-size: 13px; line-height: 22.5px; letter-spacing: .6px; color: var(--ink-soft); }

  .about { position: absolute; left: 64px; top: 809px; width: 963px; height: 283px; background: var(--band); overflow: hidden; }
  .about-curve { position: absolute; left: 0; top: 0; }
  .about-photo { position: absolute; left: 147px; top: 867px; width: 330px; height: 187px; background: var(--white); padding: 9px 8px 10px 8px; }
  .about-photo div { width: 100%; height: 100%; background: linear-gradient(90deg, #d6cbbd 0%, #f0ece6 35%, #9aa8c8 65%, #4f6fae 100%); }
  .about-text { position: absolute; left: 501px; top: 868px; width: 438px; font-size: 13px; line-height: 22.3px; letter-spacing: .6px; text-align: justify; color: var(--ink); }
  .about-text p + p { margin-top: 22.3px; }
  .read-more { position: absolute; left: 847px; top: 1055px; width: 88px; height: 26px; border-radius: 4px; background: var(--button); color: var(--white);
    font-size: 13px; letter-spacing: .6px; text-align: center; line-height: 26px; text-decoration: none; }

  .footer-nav { position: absolute; left: 0; top: 1132px; width: 1091px; height: 34px; background: var(--footer); }
  .footer-nav a { position: absolute; top: 10px; transform: translateX(-50%); font-family: "Arimo", sans-serif; font-size: 11.5px; letter-spacing: .5px; color: var(--white); text-decoration: none; white-space: nowrap; }
  .copyright { position: absolute; left: 0; top: 1166px; width: 1091px; height: 34px; background: var(--sky-deep); text-align: center;
    font-family: "Arimo", sans-serif; font-size: 10.5px; letter-spacing: .4px; line-height: 34px; color: var(--white); }
</style>
</head>
<body>
  <div class="page"></div>

  <header>
    <div class="brand"><span class="brand-dot"></span><span class="brand-name">Meadowlight<br>Home Care</span></div>
    <ul class="social" aria-label="Social links"><li></li><li></li><li></li></ul>
  </header>

  <div class="ribbon left"></div>
  <div class="ribbon right"></div>
  <svg style="position:absolute;left:41px;top:184px" width="23" height="21" aria-hidden="true"><polygon points="0,0 23,0 23,21" fill="var(--sky-fold)"/></svg>
  <svg style="position:absolute;left:1027px;top:184px" width="21" height="21" aria-hidden="true"><polygon points="0,0 21,0 0,21" fill="var(--sky-fold)"/></svg>
  <nav class="main-nav">
    <a href="#" style="left:125px">Home</a>
    <a href="#" style="left:241px">About us</a>
    <a href="#" style="left:367px">Services</a>
    <a href="#" style="left:496px">Resources</a>
    <a href="#" style="left:612px">FAQ</a>
    <a href="#" style="left:737px">Employment</a>
    <a href="#" style="left:875px">Contact</a>
  </nav>

  <section class="hero" role="img" aria-label="Photo of a smiling elderly woman in a wheelchair talking with a young caregiver">
    <h1 class="hero-title">We <em>Care</em> for you</h1>
    <p class="hero-sub">24 <em>hours a day,</em> 7 <em>days a week</em></p>
    <div class="hero-button">Check our Services
      <svg width="10" height="14" aria-hidden="true"><polyline points="2,2 8,7 2,12" fill="none" stroke="#9a9a9a" stroke-width="2.5"/></svg>
    </div>
    <div class="hero-arrow prev"><svg width="44" height="44" aria-hidden="true"><polyline points="26,12 16,22 26,32" fill="none" stroke="#fff" stroke-width="4"/></svg></div>
    <div class="hero-arrow next"><svg width="44" height="44" aria-hidden="true"><polyline points="18,12 28,22 18,32" fill="none" stroke="#fff" stroke-width="4"/></svg></div>
    <div class="hero-dots"><span></span><span></span><span></span><span></span></div>
  </section>

  <h2 class="section-title" style="top:627px">Welcome to Meadowlight Home Care</h2>
  <div class="rule" style="top:662px"></div>
  <p class="welcome-text">Lorem ipsum dolor sit amet, consectetur adipiscing elit. Morbi non eleifend nisl. Ut eget odio nec eros pretium egestas. Nunc in consectetur arcu. Duis quis lacus augue. Suspendisse potenti. Aliquam erat volutpat. Aliquam ornare, turpis ac porttitor blandit, tortor odio tincidunt ligula.</p>
  <div class="rule" style="top:767px"></div>

  <section class="about">
    <svg class="about-curve" width="963" height="283" aria-hidden="true"><path d="M0,283 C350,250 700,150 963,0 L963,283 Z" fill="var(--band-light)" opacity=".5"/></svg>
  </section>
  <h2 class="section-title" style="top:825px">About us</h2>
  <div class="rule" style="top:857px"></div>
  <div class="about-photo"><div role="img" aria-label="Photo of a nurse comforting an elderly woman seated on a sofa"></div></div>
  <div class="about-text">
    <p>Lorem ipsum dolor sit amet, consectetur adipiscing elit. Morbi non eleifend nisl. Ut eget odio nec eros pretium egestas. Nunc in consectetur arcu. Duis quis lacus augue. Suspendisse potenti. Aliquam erat volutpat. Aliquam ornare, turpis ac porttitor blandit.</p>
    <p>tortor odio tincidunt ligula, quis viverra diam libero sit amet lorem. Suspendisse eros mauris, fermentum non sapien sit amet, fermentum sodales justo. Sed pharetra.</p>
  </div>
  <a class="read-more" href="#">read more</a>

  <footer>
    <nav class="footer-nav">
      <a href="#" style="left:320px">Home</a>
      <a href="#" style="left:394px">About us</a>
      <a href="#" style="left:476px">Services</a>
      <a href="#" style="left:566px">Resources</a>
      <a href="#" style="left:639px">FAQ</a>
      <a href="#" style="left:719px">Employment</a>
      <a href="#" style="left:808px">Contact</a>
    </nav>
    <p class="copyright">Copyright © 2013 Meadowlight Home Care All rights reserved.</p>
  </footer>
</body>
</html>
```